Business Card Design

Looking for a professional looking business card for a carpentry/construction business that deals with renovations, extensions, homes, and anything carpentry based in Northern Australia. Would like to incorporate the attached logo with backgrounds of white, grey or maybe a close up of timber/wood grain. Thanks

Industry/Entity Type

Carpentry

Contact Information for Business Card

Dean Pollard, Owner, Po Box 2946 Katherine NT 0851, dean-pollard@tallmail.example, 0461907243, Builders Number: 392417CR

Requirements
Should not have
• Power tools/hand tools related to carpentry

```html
<!DOCTYPE html>
<html lang="en">
<head>
<meta charset="UTF-8">
<title>Pollard Carpentry – Business Card</title>
<link href="https://fonts.googleapis.com/css2?family=Questrial&family=Roboto:wght@300&display=swap" rel="stylesheet">
<style>
  :root {
    --card-white: #ffffff;
    --band-blue: #1c63ad;
    --brand-blue: #1f57a5;
    --text-light: #ffffff;
  }
  html, body {
    margin: 0;
    padding: 0;
    width: 1200px;
    height: 741px;
    overflow: hidden;
    background: var(--card-white);
  }
  .card {
    position: relative;
    width: 1200px;
    height: 741px;
    background: var(--card-white);
    overflow: hidden;
  }
  .brand {
    position: absolute;
    left: 72px;
    top: 112px;
    display: flex;
    align-items: center;
    gap: 18px;
  }
  .brand-mark {
    width: 56px;
    height: 56px;
    background: var(--brand-blue);
  }
  .brand-name {
    font-family: "Questrial", sans-serif;
    font-size: 52px;
    line-height: 1;
    color: var(--brand-blue);
    white-space: nowrap;
  }
  .contact-band {
    position: absolute;
    left: 0;
    top: 269px;
    width: 1200px;
    height: 472px;
    background: var(--band-blue);
  }
  .line {
    position: absolute;
    right: 69px;
    margin: 0;
    line-height: 1;
    color: var(--text-light);
    white-space: nowrap;
    text-align: right;
  }
  .person-name {
    top: 299px;
    font-family: "Questrial", sans-serif;
    font-size: 50px;
  }
  .person-role {
    top: 356px;
    font-family: "Questrial", sans-serif;
    font-size: 33px;
    font-style: italic;
  }
  .detail {
    font-family: "Roboto", sans-serif;
    font-weight: 300;
    font-size: 30px;
  }
  .phone { top: 456px; }
  .email { top: 499px; }
  .address { top: 588px; }
  .licence { top: 634px; }
</style>
</head>
<body>
  <div class="card">
    <div class="brand">
      <div class="brand-mark"></div>
      <div class="brand-name">Pollard Carpentry</div>
    </div>
    <div class="contact-band"></div>
    <p class="line person-name">Dean Pollard</p>
    <p class="line person-role">Owner</p>
    <p class="line detail phone">0461907243</p>
    <p class="line detail email">dean-pollard@tallmail.example</p>
    <p class="line detail address">Po Box 2946, Katherine NT 0851</p>
    <p class="line detail licence">Builders Number: 392417CR</p>
  </div>
</body>
</html>
```